BRIGHT COLORFUL + 55 FAMILY HISTORY BROCHURE 11 x 17 bifold

11 x 17 Bifold Flyer I have given you the Layout I just need you to make it Pretty

YOU DO NOT NEED TO FOLLOW MY LAYOUT, You can but dont have too

Target Market(s)

55 year old consumers, who could choose our service of Hereditary Cancer Screening

Industry/Entity Type

Health And Wellness

Requirements
Must have
• Must be appealing to Grand Parents, must make them want to test , show lots of pictures of grand children, YOU DO NOT NEED TO FOLLOW MY LAYOUT , You can but dont have too
Nice to have
• use our colors of our logo , YOU DO NOT NEED TO FOLLOW MY LAYOUT , You can but dont have too
Should not have
• YOU DO NOT NEED TO FOLLOW MY LAYOUT, You can but dont have too

```html
<!DOCTYPE html>
<html lang="en">
<head>
<meta charset="utf-8">
<title>Family History Brochure – Kinwell Health Circle</title>
<link href="https://fonts.googleapis.com/css2?family=Montserrat:wght@300;400;700&display=swap" rel="stylesheet">
<style>
  :root{
    --navy:#1a1d6b;
    --lime:#86e01e;
    --url-green:#2d8a14;
    --ink:#1e1e24;
    --paper:#ffffff;
    --stage:#e3e6e9;
  }
  *{box-sizing:border-box;margin:0;padding:0}
  html,body{width:1200px;height:1015px;overflow:hidden;background:var(--stage)}
  body{font-family:'Montserrat',Arial,sans-serif;color:var(--ink)}
  .spread{position:absolute;left:40px;top:145px;width:1120px;height:725px;display:flex;box-shadow:0 10px 30px rgba(0,0,0,.18)}
  .page{position:relative;width:560px;height:725px;background:var(--paper);overflow:hidden}
  .page--left{border-right:1px solid #e2e2e2}
  .band{position:absolute;left:0;right:0;bottom:0;height:62px;background:var(--lime)}
  .url{position:absolute;bottom:70px;left:0;width:100%;text-align:center;color:var(--url-green);font-size:15px;line-height:18px;letter-spacing:.2px}
  .navy-block{position:absolute;background:var(--navy)}
  .photo{position:absolute}
  .lead{color:var(--lime);font-weight:300;font-size:15px;line-height:1.3}
  .body{font-size:8.6px;line-height:1.42}
  .body p{margin-bottom:10px}
  .body p:last-child{margin-bottom:0}
  .body b,.sidebar b{font-weight:700}
  .sidebar{font-size:8.8px;line-height:1.4}

  /* left page */
  .page--left .navy-block{left:0;top:30px;width:370px;height:365px}
  .page--left .photo{left:70px;top:60px;width:440px;height:180px;
    background:linear-gradient(120deg,#d9c3b3 0%,#f2e3d9 40%,#c9875f 70%,#efe6e0 100%)}
  .page--left .lead{position:absolute;left:24px;top:254px;width:330px}
  .page--left .lead p+p{margin-top:12px}
  .page--left .sidebar{position:absolute;left:386px;top:254px;width:158px}
  .page--left .body{position:absolute;left:24px;top:410px;width:512px}

  /* right page */
  .page--right .intro{position:absolute;left:34px;top:36px;width:494px}
  .page--right .photo{left:34px;top:160px;width:492px;height:270px;
    background:linear-gradient(160deg,#4f8a2c 0%,#9cc45a 35%,#d9e4c8 60%,#7aa4cf 100%)}
  .page--right .navy-block{left:352px;top:330px;width:208px;height:333px}
  .page--right .lead{position:absolute;left:368px;top:448px;width:178px;font-size:13.5px}
  .page--right .sidebar{position:absolute;left:112px;top:448px;width:225px}
  .page--right .url{width:352px}
  .brand{position:absolute;left:372px;top:568px;display:flex;align-items:center;gap:10px;color:#fff;font-weight:700;font-size:16px;line-height:1.05;letter-spacing:.5px}
  .brand-dot{width:36px;height:36px;border:2px solid #fff;border-radius:50%}
</style>
</head>
<body>
<main class="spread">

  <section class="page page--left">
    <div class="navy-block"></div>
    <div class="photo" role="img" aria-label="Grandmother and mother smiling over a sleeping newborn"></div>
    <div class="lead">
      <p>A Positive result or finding a mutation is Not a Cancer Diagnosis and does not mean you will ever develop Cancer.</p>
      <p>Learning if you have an increased risk for cancer can make a difference.</p>
    </div>
    <div class="sidebar">
      <b>Genetic testing revealed</b> Daniel Marsh carried a mutation that gave him a 55 to 70 percent chance of developing stomach cancer. Early screening revealed there were 14 sites of stage 1A cancer. Once the news sunk in, he realized <b>his Mother Genetic Testing Saved His Life.</b>
    </div>
    <div class="body">
      <p><b>Genetic Testing Saved My Life.</b> Because of my age and <b>Ashkenazi Jewish ancestry,</b> My Dr recommended Genetic Testing and they were right. I had the BRCA Gene, because of this my other two sister got tested, my younger sister was positive and my older sister was negative. <b>Now we are in control,</b> there are steps that can be taken to reduce the risks, including enhanced breast cancer screening, risk-reducing surgeries, and chemoprevention, in which drugs are used to try to reduce the risk or delay the development of cancer.</p>
      <p><b>A breast cancer survivor before age 30:</b> 'Genetic testing saved my life' Megan Hale was diagnosed with breast cancer two weeks before her 29th birthday. Hale, now 30, credits her recovery to <b>awareness</b> of a <b>hereditary genetic mutation</b> that predisposed her and her family to the disease. <b>After my mom tested positive for the BRCA 1 gene mutation,</b> I knew genetic testing was something that I would need. <b>Once I tested positive,</b> I was referred to a breast health clinic for increased surveillance. There, my medical care providers were very diligent in making sure I was watched closely. <b>Knowledge is power</b> and, in this case, <b>Genetic testing saved my life!</b></p>
      <p><b>My father had genetic testing</b> and found he had hereditary nonpolyposis colorectal cancer (HNPCC) commonly known as Lynch syndrome. My name is Laura Finch and I am a 10-year survivor of colorectal cancer. From an early age I learned the importance of screenings and knew about signs and symptoms. <b>Following screening guidelines for individuals at an increased risk &amp; Knowing my family history saved my life!</b></p>
    </div>
    <div class="url">www.familyriskcheck.example</div>
    <div class="band"></div>
  </section>

  <section class="page page--right">
    <div class="intro body">
      <p><b>Genetic Testing</b> is done to determine whether family members without obvious illness have inherited the same mutation as a family member who is known to carry a cancer associated mutation. Meaning <b>Will You Help Your Kids &amp; Grand Children.</b></p>
      <p><b>What are the benefits of testing?</b> "The Power of Knowledge" <b>Helping Younger Family Members Know if there is a Risk and Preparing for it.</b> knowing if you have a genetic mutation is that you can work with your doctor to monitor and address your cancer risks. <b>According to the National Cancer Council eating 5 or more Servings of Vegetables &amp; Fruit, and Most Importantly also lowering your intake of red meat, dairy and eggs will help prevent or delay cancer.</b></p>
    </div>
    <div class="navy-block"></div>
    <div class="photo" role="img" aria-label="Three generations of a family smiling together outdoors in a green park"></div>
    <div class="sidebar">
      <b>There are many benefits to getting tested,</b> regardless of the eventual result. If one of your family members — however distant — had cancer, there is a chance that you inherited a gene mutation that not only increases your personal risk of cancer, but also could be passed to the next generation. Those who are carriers of hereditary cancer gene mutations, could be at risk of getting cancer earlier in life than the general population. <b>The sooner genetic testing is done, the more likely it is that the risk can be managed appropriately.</b>
    </div>
    <p class="lead">There are many Known risk factors for Cancer. GENETICS and FAMILY HISTORY are Often Overlooked.</p>
    <div class="brand"><span class="brand-dot"></span><span>KINWELL<br>HEALTH<br>CIRCLE</span></div>
    <div class="url">www.familyriskcheck.example</div>
    <div class="band"></div>
  </section>

</main>
</body>
</html>
```